Wine and retail website for a high-end resort community

We are introducing a line of quality wines in the resort community of Martha's Vineyard, Massachusetts, USA. The site will detail information about the wine, and online store connected to and external government approved shipper for wine, and additional non-alcoholic retail merchandise sales.

We are planning the site to be driven off the Squarespace platform so I do not believe coding is necessary initially; however, the ability to do sop would be helpful if needed.

Attached are the images/files we have available so far. Please feel free to use stock images in your design.

Target Market(s)

Wine enthusiasts in the resort community of Martha’s Vineyard Massachusetts

Industry/Entity Type

Wine

Number of Pages Required

4 page

Font styles to use
Sans Serif

Requirements
Must have
• Home page, about page, wine page, e-commerce page, retail merchandise page. I recently came across brelmorcellars.com and really like the look and layout of their pages if that helps
Nice to have
• A short wine/Martha’s Vineyard related video on the home page

```html
<!DOCTYPE html>
<html lang="en">
<head>
<meta charset="utf-8">
<title>Harbor Ridge Estates</title>
<link rel="stylesheet" href="https://fonts.googleapis.com/css2?family=DM+Sans:wght@400;500;700&family=Playfair+Display:wght@400;700&family=Mrs+Saint+Delafield&display=swap">
<style>
:root{
  --wine:#8e1f2b;
  --ink:#1e1e1e;
  --muted:#555;
  --cream:#f8f5ec;
  --footer:#1b1c17;
  --white:#fff;
}
*{box-sizing:border-box;margin:0;padding:0}
html,body{width:1200px;height:3088px;overflow:hidden}
body{position:relative;background:var(--white);font-family:"DM Sans",sans-serif;color:var(--ink)}
.abs{position:absolute}
.serif{font-family:"Playfair Display",serif}
.script{font-family:"Mrs Saint Delafield",cursive;color:var(--wine)}

/* header */
.site-header{position:absolute;left:0;top:0;width:1200px;height:109px;background:var(--white)}
.brand{position:absolute;left:130px;top:34px;width:140px;text-align:center;font-family:"Playfair Display",serif;font-size:20px;line-height:22px;color:var(--ink)}
.brand small{display:block;font-size:9px;letter-spacing:4px;line-height:14px}
.nav{position:absolute;top:51px;font-family:"Playfair Display",serif;font-size:15px;color:var(--ink)}
.nav-active{position:absolute;left:354px;top:4px;width:2px;height:38px;background:var(--wine)}
.call-label{position:absolute;left:798px;top:33px;font-size:10px;color:#777}
.call-number{position:absolute;left:797px;top:47px;font-family:"Playfair Display",serif;font-size:21px}
.icon-box{position:absolute;left:964px;top:36px;width:90px;height:41px;border:1px solid #ccc}
.icon-box::after{content:"";position:absolute;left:44px;top:0;width:1px;height:39px;background:#ccc}
.cart-count{position:absolute;left:1034px;top:55px;width:13px;height:13px;border-radius:50%;background:var(--wine);color:#fff;font-size:8px;text-align:center;line-height:13px}

/* hero */
.hero{position:absolute;left:0;top:109px;width:1200px;height:604px;background:linear-gradient(180deg,#5d6a3b 0%,#6f7a3a 22%,#3d4a1f 45%,#2e3417 70%,#4a3a24 100%)}
.hero-script{position:absolute;top:310px;width:1200px;text-align:center;font-size:54px;color:#fff}
.hero-title{position:absolute;top:370px;width:1200px;text-align:center;font-family:"Playfair Display",serif;font-weight:700;font-size:57px;color:#fff}
.btn-discover{position:absolute;left:530px;top:460px;width:141px;height:40px;background:var(--wine);color:#fff;font-size:13px;font-weight:500;text-align:center;line-height:40px}
.notch{position:absolute;width:0;height:0;border-left:14px solid transparent;border-right:14px solid transparent}

/* welcome */
.section-script{position:absolute;width:1200px;text-align:center;font-size:44px}
.rule{position:absolute;height:1px;background:var(--wine)}
.section-title{position:absolute;width:1200px;text-align:center;font-family:"Playfair Display",serif;font-size:30px}
.welcome-copy{position:absolute;left:225px;top:866px;width:750px;text-align:center;font-size:14.5px;line-height:24px;color:#444}
.card{position:absolute;top:997px;width:289px;height:370px}
.card span{position:absolute;left:0;bottom:14px;width:100%;text-align:center;font-family:"Playfair Display",serif;font-size:25px;color:#fff}

/* video */
.video{position:absolute;left:0;top:1440px;width:1200px;height:520px;background:linear-gradient(180deg,#1f2f42 0%,#2a3a40 35%,#2b3a22 60%,#37401f 100%)}
.video-title{position:absolute;top:1608px;width:1200px;text-align:center;font-family:"Playfair Display",serif;font-weight:700;font-size:40px;color:#fff}
.play{position:absolute;left:562px;top:1696px;width:60px;height:60px;border-radius:50%;background:#fff}
.play-text{position:absolute;left:540px;top:1785px;font-size:38px;color:#fff}

/* shop */
.shop{position:absolute;left:0;top:1960px;width:1200px;height:668px;background:var(--cream)}
.shop-intro{position:absolute;left:403px;top:2043px;width:380px;font-size:12.5px;line-height:24px;color:#444}
.btn-shop{position:absolute;left:894px;top:2048px;width:161px;height:34px;border:1px solid var(--wine);border-left-width:3px;color:var(--wine);font-size:11px;font-weight:700;letter-spacing:2px;line-height:32px;padding-left:20px}
.bottle{position:absolute;top:2165px;width:84px;height:305px;border-radius:18px 18px 8px 8px}
.product-name{position:absolute;top:2498px;width:300px;text-align:center;font-family:"Playfair Display",serif;font-size:16px}
.price{position:absolute;top:2533px;width:300px;text-align:center;font-size:14.5px;font-weight:500}
.price s{color:#999;font-weight:400;margin-right:4px}
.round{position:absolute;width:34px;height:34px;border-radius:50%;border:1px solid var(--wine);background:#fff}
.next{position:absolute;left:1057px;top:2336px;width:34px;height:34px;border-radius:50%;background:#fff;border:1px solid #e5e0d4}

/* footer */
.site-footer{position:absolute;left:0;top:2628px;width:1200px;height:460px;background:var(--footer)}
.footer-brand{position:absolute;top:2735px;width:1200px;text-align:center;font-family:"Playfair Display",serif;font-size:27px;line-height:28px;color:#fff}
.footer-brand small{display:block;font-size:10px;letter-spacing:5px;line-height:18px}
.col-title{position:absolute;top:2856px;width:360px;text-align:center;font-family:"Playfair Display",serif;font-size:16px;color:#fff}
.col-text{position:absolute;top:2900px;width:360px;text-align:center;font-size:14px;line-height:24px;color:#fff}
.divider{position:absolute;top:2858px;width:1px;height:84px;background:#444}
.copyright{position:absolute;top:3036px;width:1200px;text-align:center;font-size:10.5px;color:#8a8a80}
</style>
</head>
<body>

<header class="site-header">
  <div class="brand">Harbor Ridge<small>ESTATES</small></div>
  <div class="nav-active"></div>
  <a class="nav" style="left:338px">Wine</a>
  <a class="nav" style="left:401px">Wine Club</a>
  <a class="nav" style="left:496px">News</a>
  <a class="nav" style="left:557px">Our Story</a>
  <a class="nav" style="left:650px">Contact</a>
  <svg class="abs" style="left:746px;top:38px" width="36" height="36" viewBox="0 0 36 36" fill="none" stroke="#222" stroke-width="1.6"><path d="M8 5l5 6-3 3c2 5 6 9 11 11l3-3 6 5-4 4C15 31 5 21 4 9z"/><path d="M22 4a10 10 0 0 1 10 10"/><path d="M22 9a5 5 0 0 1 5 5"/></svg>
  <div class="call-label">Call us now</div>
  <div class="call-number">800-555-01472</div>
  <div class="icon-box"></div>
  <svg class="abs" style="left:976px;top:45px" width="20" height="22" viewBox="0 0 20 22" fill="none" stroke="#222" stroke-width="1.5"><circle cx="10" cy="7" r="5"/><path d="M2 21c0-5 4-8 8-8s8 3 8 8"/></svg>
  <svg class="abs" style="left:1020px;top:45px" width="20" height="22" viewBox="0 0 20 22" fill="none" stroke="#222" stroke-width="1.5"><rect x="2" y="7" width="16" height="14" rx="2"/><path d="M6 9V5a4 4 0 0 1 8 0v4"/></svg>
  <div class="cart-count">0</div>
</header>

<section class="hero" role="img" aria-label="Photo of vineyard rows stretching toward rolling fields at golden hour"></section>
<div class="rule" style="left:455px;top:352px;width:28px;background:#fff"></div>
<div class="rule" style="left:716px;top:352px;width:28px;background:#fff"></div>
<div class="hero-script script" style="color:#fff">Tasty wine form</div>
<h1 class="hero-title">Harbor Ridge Estate</h1>
<a class="btn-discover">Discover More</a>
<div class="notch" style="left:586px;top:699px;border-bottom:14px solid var(--white)"></div>

<div class="section-script script" style="top:738px">Welcome to</div>
<div class="rule" style="left:475px;top:775px;width:34px"></div>
<div class="rule" style="left:663px;top:775px;width:34px"></div>
<h2 class="section-title" style="top:795px">Harbor Ridge Estates</h2>
<p class="welcome-copy">Harbor Ridge Estates Cabernet Sauvignon shows aromas of oak, baking spice, and cassis. On the palate, tones of black cherry and a hint of cinnamon, nutmeg and French Vanilla leave a delicious lasting finish.We hope our wines are a reminder of good times and good company spent on the Vineyard. Here’s to keeping it on island time!</p>

<a class="card" style="left:145px;background:linear-gradient(180deg,#8a9a6a 0%,#6a7a3e 40%,#9a7a55 100%)" role="img" aria-label="Photo of two vintners walking through vineyard rows carrying a crate of grapes"><span>Our Story</span></a>
<a class="card" style="left:456px;background:linear-gradient(180deg,#0e0d0c 0%,#2a201a 55%,#6a6258 100%)" role="img" aria-label="Photo of a plated salad with a glass of white wine and a bottle on a dark table"><span>Make Reservation</span></a>
<a class="card" style="left:766px;background:linear-gradient(180deg,#7f9ab5 0%,#4e6f3c 45%,#6a4a45 100%)" role="img" aria-label="Photo of friends raising red wine glasses in a toast outdoors"><span>Wine Club</span></a>

<section class="video" role="img" aria-label="Dim photo of a grassy coastal dune with a lighthouse at dusk"></section>
<h2 class="video-title">Know More Abour Harbor Ridge Estates</h2>
<div class="play"></div>
<svg class="abs" style="left:584px;top:1716px" width="20" height="20" viewBox="0 0 20 20"><path d="M3 1l15 9-15 9z" fill="var(--wine)"/></svg>
<div class="play-text script" style="color:#fff">Play Video</div>
<svg class="abs" style="left:640px;top:1765px" width="20" height="40" viewBox="0 0 20 40" fill="none" stroke="#fff" stroke-width="1.2"><path d="M4 38c12-10 12-24 6-34M10 4l-4 4M10 4l3 5"/></svg>
<div class="notch" style="left:586px;top:1946px;border-bottom:14px solid var(--cream)"></div>

<section class="shop"></section>
<div class="abs script" style="left:145px;top:1996px;font-size:46px">Shop</div>
<div class="rule" style="left:232px;top:2034px;width:36px"></div>
<h2 class="abs serif" style="left:145px;top:2060px;font-size:30px;font-weight:400">Our Wines</h2>
<p class="shop-intro">Join our family of wine lovers and be the first to taste our new releases and attend special events.</p>
<a class="btn-shop">GO TO SHOP</a>
<svg class="abs" style="left:1020px;top:2058px" width="16" height="12" viewBox="0 0 16 12" fill="none" stroke="var(--wine)" stroke-width="1.4"><path d="M0 6h15M10 1l5 5-5 5"/></svg>

<div class="bottle" style="left:248px;background:linear-gradient(90deg,#5a5a1e,#8a8a3a 40%,#4a4a18)" role="img" aria-label="Bottle of white wine"></div>
<div class="bottle" style="left:558px;background:linear-gradient(90deg,#e89a90,#f6c4ba 40%,#e08a80)" role="img" aria-label="Bottle of rosé wine"></div>
<div class="bottle" style="left:868px;background:linear-gradient(90deg,#0d0d0d,#2a2a2a 40%,#0a0a0a)" role="img" aria-label="Bottle of red wine"></div>

<div class="round" style="left:533px;top:2443px"></div>
<div class="round" style="left:583px;top:2443px"></div>
<div class="round" style="left:632px;top:2443px"></div>
<svg class="abs" style="left:543px;top:2452px" width="14" height="16" viewBox="0 0 14 16" fill="none" stroke="var(--wine)" stroke-width="1.3"><rect x="1" y="5" width="12" height="10" rx="1"/><path d="M4 6V4a3 3 0 0 1 6 0v2"/></svg>
<svg class="abs" style="left:591px;top:2454px" width="18" height="12" viewBox="0 0 18 12" fill="none" stroke="var(--wine)" stroke-width="1.3"><path d="M1 6c4-6 12-6 16 0-4 6-12 6-16 0z"/><circle cx="9" cy="6" r="2.5"/></svg>
<svg class="abs" style="left:641px;top:2453px" width="16" height="14" viewBox="0 0 16 14" fill="none" stroke="var(--wine)" stroke-width="1.3"><path d="M8 13L2 7a3.5 3.5 0 0 1 6-4 3.5 3.5 0 0 1 6 4z"/></svg>

<div class="product-name" style="left:140px">2019 Vineyards Napa Valley</div>
<div class="price" style="left:135px">$35.00</div>
<div class="product-name" style="left:450px">2020 Limited Release Le Rosé</div>
<div class="price" style="left:450px"><s>$ 59.00</s> $46.00</div>
<div class="product-name" style="left:760px">2019 Vineyards Napa Valley</div>
<div class="price" style="left:755px">$35.00</div>
<div class="next"></div>
<svg class="abs" style="left:1070px;top:2347px" width="8" height="12" viewBox="0 0 8 12" fill="none" stroke="#333" stroke-width="1.3"><path d="M1 1l5 5-5 5"/></svg>

<footer class="site-footer" role="img" aria-label="Dark photo of vineyard foliage behind the footer"></footer>
<div class="notch" style="left:586px;top:2628px;border-top:14px solid var(--cream)"></div>
<div class="footer-brand">Harbor Ridge<small>ESTATES</small></div>
<div class="col-title" style="left:55px">Call us</div>
<div class="col-text" style="left:45px">+(1) 508 555 0142<br>+(1) 508 555 0187</div>
<div class="divider" style="left:400px"></div>
<div class="col-title" style="left:420px">Our Location</div>
<div class="col-text" style="left:420px">14 Tidewater Lane, WEST TISBURY,<br>MA 02575</div>
<div class="divider" style="left:776px"></div>
<div class="col-title" style="left:748px">Email us</div>
<div class="col-text" style="left:765px">hello@harborridgeestates.com</div>
<div class="copyright">Copyright © 2020, Harbor Ridge Estates.com. All right reserved</div>

</body>
</html>
```